Business Card Design

I need a business card for a company based in London, UK. I provide garden design, landscaping and maintenance services. The company specialises in modern, urban gardens. It must be horizontal design, white paper and black simple (easy to read) font. The print must be on clear, white surrounding. I like design that use the colours black, yellow, grey and different shades of green. The design must be tidy. It must not be overloaded with decorating. Embodied a small picture of a fragment of garden or plant or leaf in the sun (it must be yellowish and greenish). It would be good if it's "live and energetic". I attached all text and logo that have to appear on the card.

Target Market(s)

architect, property designers, property management companies, large property owners

Industry/Entity Type

Landscaping

Contact Information for Business Card

All the text must be the same as on my old card which I attached.

Requirements
Must have
• modern, simple, tidy, professional look
green, yellow, black colours,
white surrounding,
simple readable black font on clear white surrounding,
a small picture of garden or plant or "sun lights through the tree canopy"
Nice to have
• graduate movement from light green to dark green
Should not have
• old style font,
text must no be placed on pictures or decorations,
red and blue colours,
picture on the reverse

```html
<!DOCTYPE html>
<html lang="en">
<head>
<meta charset="utf-8">
<title>Brightleaf Landscapes – Business Card</title>
<link rel="stylesheet" href="https://fonts.googleapis.com/css2?family=Questrial&family=Arimo:wght@400&display=swap">
<style>
  :root {
    --backdrop: #e6e6e4;
    --paper: #ffffff;
    --ink: #1a1a1a;
    --ink-soft: #3a3a3a;
    --ink-muted: #666666;
    --green-dark: #2f8a40;
    --green-mid: #5fae3f;
    --green-light: #8cc63f;
    --green-pale: #c6e08c;
    --green-paler: #d8ec9e;
    --yellow: #eee82a;
  }
  * { box-sizing: border-box; margin: 0; padding: 0; }
  html, body {
    width: 1200px; height: 805px; overflow: hidden;
    background: var(--backdrop);
  }
  .sheet { position: relative; width: 1200px; height: 805px; }
  .card {
    position: absolute; top: 234px;
    width: 520px; height: 336px;
    background: var(--paper);
    box-shadow: 0 6px 22px rgba(0,0,0,.18);
    overflow: hidden;
  }
  .card--front { left: 50px; font-family: "Questrial", sans-serif; color: var(--ink); }
  .card--back  { left: 630px; font-family: "Arimo", sans-serif; color: var(--ink); }

  /* front */
  .company {
    position: absolute; right: 36px; top: 52px;
    font-size: 26px; line-height: 1; color: var(--ink);
  }
  .services-line {
    position: absolute; right: 36px; top: 98px;
    display: flex; gap: 18px;
    font-size: 16px; color: var(--ink-muted);
  }
  .person {
    position: absolute; left: 30px; top: 166px;
    font-size: 23px; font-weight: 400;
  }
  .contact {
    position: absolute; top: 214px;
    font-size: 13.5px; line-height: 15px;
  }
  .contact--left { left: 30px; }
  .contact--right { left: 268px; }
  .contact__group + .contact__group { margin-top: 14px; }
  .grass-band {
    position: absolute; left: 0; right: 0; bottom: 0; height: 42px;
    background: linear-gradient(to top, var(--green-dark), var(--green-light) 70%, rgba(140,198,63,0));
  }

  /* back */
  .services { position: absolute; left: 0; top: 28px; right: 70px; }
  .service { position: relative; height: 56px; padding: 10px 0 0 46px; }
  .service__swatch { position: absolute; left: 0; top: 0; width: 26px; height: 50px; }
  .service--1 .service__swatch { background: var(--green-dark); }
  .service--2 .service__swatch { background: var(--green-mid); }
  .service--3 .service__swatch { background: var(--green-pale); }
  .service--4 .service__swatch { background: var(--green-paler); }
  .service--5 .service__swatch { background: var(--yellow); }
  .service__title { font-size: 15px; line-height: 18px; font-weight: 400; }
  .service__detail { font-size: 9px; line-height: 13px; color: var(--ink-soft); }
  .grass-corner {
    position: absolute; right: 0; top: 0; width: 62px; height: 150px;
    background: linear-gradient(to left, var(--green-dark), var(--green-light) 60%, rgba(140,198,63,0));
  }
</style>
</head>
<body>
<main class="sheet">

  <section class="card card--front" aria-label="Business card, front">
    <p class="company">Brightleaf Landscapes</p>
    <p class="services-line"><span>design</span><span>landscaping</span><span>maintenance</span></p>

    <h1 class="person">Daniel Morrow</h1>

    <div class="contact contact--left">
      <p class="contact__group">02079460123<br>07700900456</p>
      <p class="contact__group">www.brightleaf-landscapes.co.uk<br>info@brightleaf-landscapes.co.uk</p>
    </div>
    <p class="contact contact--right">42 Mill Lane,<br>Richmond, TW9 4PQ</p>

    <div class="grass-band" role="img" aria-label="Band of green grass blades along the bottom edge"></div>
  </section>

  <section class="card card--back" aria-label="Business card, back">
    <div class="services">
      <div class="service service--1">
        <span class="service__swatch"></span>
        <h2 class="service__title">Garden Design</h2>
        <p class="service__detail">all styles; hand-drawn &amp; CAD, detailed mapping, underground service tracing, soil analysis</p>
      </div>
      <div class="service service--2">
        <span class="service__swatch"></span>
        <h2 class="service__title">Garden Maintenance</h2>
        <p class="service__detail">lawn care programs, improving the soil, plant health issues, clearance, tree husbandry</p>
      </div>
      <div class="service service--3">
        <span class="service__swatch"></span>
        <h2 class="service__title">Grounds Maintenance</h2>
        <p class="service__detail">algae, moss &amp; pest control, drainage improvements; green areas, car parks, playgrounds.</p>
      </div>
      <div class="service service--4">
        <span class="service__swatch"></span>
        <h2 class="service__title">Patios, Fences, Decking</h2>
        <p class="service__detail">railings, walls, driveways, summerhouses; hard &amp; soft wood, natural stone, steps</p>
      </div>
      <div class="service service--5">
        <span class="service__swatch"></span>
        <h2 class="service__title">Ponds, Irrigation, Lighting</h2>
        <p class="service__detail">rockeries, water features; garden lighting, irrigation systems</p>
      </div>
    </div>
    <div class="grass-corner" role="img" aria-label="Tuft of green grass in the top right corner"></div>
  </section>

</main>
</body>
</html>
```